Mock Up Landing Page for TideGuardHoods.com

Project Description:
Were looking to update one of our landing pages to be more modern and dynamic. We want each component to be "boxed" or so when it translates to mobile we can make each component dynamic. Simple use what we have, take a look at what we want and merge the two together the best you can.
Components to include:
- Main Banner showcasing a picture and selling points of the product
- The price and ad to cart feature
- Product Description
- Reviews
- A Place to Enter Year Make and Model of customers vehicle
- A section for other products you may like (will be featuring 2 products)
- It would be a huge bonus if you incorporated a button to call in as well as chat with a representative in a clean but very noticeable way.
Current Landing Page:
https://www.tideguardhoods.com/index.php/tide-guard-trade-5l-car-cover-517204.html
Reference:
http://www.drivornix.com/car-covers/73B2118B0B0.aspx
Notes:

```html
<!DOCTYPE html>
<html lang="en">
<head>
<meta charset="utf-8">
<title>Tide Guard Hoods – 5L Car Cover</title>
<link href="https://fonts.googleapis.com/css2?family=Work+Sans:wght@500;600;700;800&family=Source+Sans+3:wght@400;600;700&display=swap" rel="stylesheet">
<style>
:root{
  --navy:#0b2f4a;
  --red:#a81010;
  --yellow:#d4d000;
  --blue:#1a8ae6;
  --grey:#d9d9d9;
  --hero:#f2f2f2;
  --gold:#f2b705;
  --orange:#f47c20;
  --black:#000;
  --white:#fff;
  --ink:#1d2a36;
}
*{margin:0;padding:0;box-sizing:border-box}
html,body{width:1200px;height:1200px;overflow:hidden;background:var(--white)}
body{font-family:"Source Sans 3",sans-serif;color:var(--ink)}
.stage{position:absolute;left:0;top:0;width:1500px;height:1500px;transform:scale(.8);transform-origin:0 0}
.page{position:absolute;left:300px;top:0;width:900px;height:1500px}
.abs{position:absolute}
.band{position:absolute;left:0;width:900px}

/* header */
.header{top:0;height:67px;background:var(--white)}
.brand-name{left:92px;top:18px;font-family:"Source Sans 3",sans-serif;font-weight:700;font-size:26px;color:var(--navy);line-height:1}
.cart{left:527px;top:22px;display:flex;align-items:center;gap:7px;font-family:"Work Sans",sans-serif;font-weight:600;font-size:11px;color:var(--navy)}
.cart-icon{width:24px;height:24px;border-radius:50%;background:#8a8f94;display:flex;align-items:center;justify-content:center}
.divider{left:640px;top:19px;width:1px;height:30px;background:#9aa3ab}
.phone{left:650px;top:14px;font-family:"Work Sans",sans-serif;font-weight:600;font-size:22px;color:var(--navy);letter-spacing:.5px}
.hours{left:658px;top:39px;font-family:"Work Sans",sans-serif;font-weight:600;font-size:9.5px;color:var(--navy)}

/* vehicle selector */
.selector{top:67px;height:34px;background:var(--navy)}
.select{top:9px;width:99px;height:16px;background:var(--white);font-size:8.5px;color:#8a8f94;padding:2px 5px}
.select::after{content:"";position:absolute;right:0;top:0;width:19px;height:16px;background:var(--gold)}
.select svg{position:absolute;right:5px;top:5px;z-index:1}

/* hero */
.hero{top:101px;height:258px;background:var(--hero)}
.hero-photo{left:80px;top:0;width:450px;height:258px;background:radial-gradient(ellipse at 50% 55%,#d4d6d8 0%,#ebecec 45%,#f4f4f4 75%)}
.info{left:567px;top:27px;width:234px;height:204px;background:var(--navy);color:var(--white);padding:10px 11px}
.info h2{font-family:"Work Sans",sans-serif;font-weight:600;font-size:17px}
.info .price{font-family:"Work Sans",sans-serif;font-weight:600;font-size:19px;margin:8px 0 6px}
.info p{font-family:"Work Sans",sans-serif;font-size:9.5px;line-height:20px}
.info .sale{font-family:"Work Sans",sans-serif;font-weight:800;font-size:44px;text-align:center;margin-top:4px;letter-spacing:1px}

/* description */
.description{top:382px;height:295px;background:var(--red)}
.photo-cover{left:90px;top:370px;width:286px;height:319px;background:linear-gradient(140deg,#e8e8e8 0%,#b9bcbf 45%,#3f8fd0 75%,#2a6fb3 100%);z-index:2}
.desc-text{left:407px;top:410px;width:405px;color:var(--white)}
.desc-text h2{font-family:"Work Sans",sans-serif;font-weight:600;font-size:13px;margin-bottom:16px}
.desc-text .lead{font-size:7.4px;line-height:13px;margin-bottom:16px}
.features{list-style:none;font-size:7.4px}
.features li{position:relative;padding-left:14px;height:18px;line-height:10px}
.features li::before{content:"";position:absolute;left:0;top:3px;width:5px;height:5px;background:var(--white)}
.btn-outline{display:inline-block;border:1px solid var(--white);color:var(--white);font-family:"Work Sans",sans-serif;font-weight:600;font-size:8px;padding:6px 18px;margin-top:9px}

/* reviews */
.reviews{top:677px;height:295px;background:var(--yellow)}
.photo-draped{left:524px;top:665px;width:286px;height:319px;background:radial-gradient(ellipse at 60% 65%,#dcdcf0 0%,#a9a9c6 40%,#111 80%);z-index:2}
.rev{left:90px;top:711px;width:388px}
.rev h2{font-family:"Work Sans",sans-serif;font-weight:600;font-size:12.5px;color:var(--ink);margin-bottom:22px}
.review{padding-bottom:14px}
.review + .review{border-top:1px solid #8c8a00;padding-top:12px}
.review-name{font-family:"Work Sans",sans-serif;font-weight:600;font-size:9.5px;color:var(--ink)}
.stars{color:#e03a2f;font-size:8px;letter-spacing:3px;margin-left:4px}
.review p{font-size:7.4px;line-height:17px;color:var(--ink);margin-top:4px}
.btn-dark{display:inline-block;border:1px solid var(--ink);color:var(--ink);font-family:"Work Sans",sans-serif;font-size:8px;padding:6px 18px;margin-top:8px}

/* products */
.products{top:972px;height:272px;background:var(--blue)}
.products h2{position:absolute;top:47px;width:900px;text-align:center;font-family:"Work Sans",sans-serif;font-weight:600;font-size:12.5px;color:var(--white)}
.card{top:92px;height:146px;display:flex}
.card-photo{width:168px;height:146px;background:radial-gradient(circle at 50% 50%,#b9bbbd 0%,#dcdddd 40%,#fff 72%)}
.card-body{width:180px;background:var(--navy);color:var(--white);padding:18px 13px}
.card-body h3{font-family:"Source Sans 3",sans-serif;font-weight:600;font-size:12px;margin-bottom:17px;white-space:nowrap}
.card-body .free{color:var(--orange);font-family:"Source Sans 3",sans-serif;font-weight:600;font-size:9.5px;margin-bottom:5px}
.card-body ul{list-style:none;font-size:7.4px}
.card-body li{position:relative;padding-left:10px;height:18px;line-height:10px}
.card-body li::before{content:"";position:absolute;left:0;top:3px;width:4px;height:4px;border-radius:50%;background:var(--white)}

/* signup */
.signup{top:1244px;height:52px;background:var(--grey)}
.signup-label{left:186px;top:18px;font-family:"Source Sans 3",sans-serif;font-weight:600;font-size:12px;color:var(--blue)}
.signup-input{left:371px;top:14px;width:262px;height:22px;background:var(--white);border:1px solid var(--blue)}
.signup-btn{left:645px;top:14px;width:67px;height:22px;background:var(--orange);color:var(--navy);font-family:"Source Sans 3",sans-serif;font-weight:600;font-size:10px;text-align:center;line-height:22px}

/* footer */
.footer{top:1296px;height:204px;background:var(--black);color:var(--white)}
.col{top:18px}
.col h4{font-family:"Source Sans 3",sans-serif;font-weight:600;font-size:9px;margin-bottom:14px}
.col ul{list-style:none;font-size:7px}
.col li{position:relative;padding-left:10px;height:18px;line-height:9px}
.col li::before{content:"";position:absolute;left:0;top:2px;width:4px;height:4px;background:var(--white)}
.chat{left:522px;top:149px;width:112px;height:17px;background:#e0241c;display:flex;align-items:center;gap:9px;padding-left:5px;font-family:"Work Sans",sans-serif;font-weight:600;font-size:7.5px}
.payments{left:681px;top:144px;width:129px;height:23px;background:var(--white);border:1px solid #ccc;display:flex;gap:3px;padding:3px}
.payments span{flex:1;background:#c7ccd3;border-radius:2px}
.footer-rule{left:0;top:176px;width:900px;height:1px;background:#333}
.copy{left:0;top:183px;width:900px;text-align:center;font-size:7px}
.copy b{color:var(--blue);font-weight:400}
</style>
</head>
<body>
<div class="stage">
<div class="page">

  <header class="band header">
    <div class="abs brand-name">Tide Guard Hoods</div>
    <div class="abs cart">
      <span class="cart-icon"><svg width="14" height="12" viewBox="0 0 14 12"><path d="M1 1h2l2 7h6l2-5H4" fill="none" stroke="#fff" stroke-width="1.3"/><circle cx="6" cy="10.5" r="1" fill="#fff"/><circle cx="10" cy="10.5" r="1" fill="#fff"/></svg></span>
      My Cart (0) <svg width="7" height="5" viewBox="0 0 7 5"><path d="M0 0h7L3.5 5z" fill="#0b2f4a"/></svg>
    </div>
    <div class="abs divider"></div>
    <div class="abs phone">800-555-0147</div>
    <div class="abs hours">Hours(M-S,10am-6:30pm EST)</div>
  </header>

  <nav class="band selector">
    <div class="abs select" style="left:461px">Select Year<svg width="8" height="5" viewBox="0 0 8 5"><path d="M0 0h8L4 5z" fill="#fff"/></svg></div>
    <div class="abs select" style="left:575px">Select Make<svg width="8" height="5" viewBox="0 0 8 5"><path d="M0 0h8L4 5z" fill="#fff"/></svg></div>
    <div class="abs select" style="left:690px">Select Model<svg width="8" height="5" viewBox="0 0 8 5"><path d="M0 0h8L4 5z" fill="#fff"/></svg></div>
  </nav>

  <section class="band hero">
    <div class="abs hero-photo" role="img" aria-label="Car wrapped in a silver fitted cover"></div>
    <div class="abs info">
      <h2>Products Info</h2>
      <div class="price">$149.99</div>
      <p>Regular Price: $349.99</p>
      <p>You Save: $200.00</p>
      <p>Availablity: In Stock</p>
      <p>Ships:24 Mar 2016</p>
      <div class="sale">SALE</div>
    </div>
  </section>

  <section class="band description"></section>
  <div class="abs photo-cover" role="img" aria-label="Silver cover being pulled off a blue car"></div>
  <div class="abs desc-text">
    <h2>Product Description</h2>
    <p class="lead">Tide Guard™ 5L Covers are the most powerful car covers available. These covers provide all season indoor and outdoor protection. Leveraging 5 impenetrable multi-layer fabrics, they offer unmatched strength and durability. The cover also features a fleece interior protecting your car's exterior finish.</p>
    <ul class="features">
      <li>Great cover for Hail Protection.</li>
      <li>10 year warranty.</li>
      <li>5 Layers of protection.</li>
      <li>Ultrasonically welded seams for 100% waterproof cover.</li>
      <li>Micro-porous film promotes breathability and prevents mildew and rotting.</li>
      <li>Soft fleece interior lining protects your car's exterior finish.</li>
    </ul>
    <span class="btn-outline">Read More</span>
  </div>

  <section class="band reviews"></section>
  <div class="abs photo-draped" role="img" aria-label="Car under a draped satin cover on a dark background"></div>
  <div class="abs rev">
    <h2>Reviews</h2>
    <div class="review">
      <span class="review-name">Marcus</span><span class="stars">★★★★★</span>
      <p>"This item is quite heavy duty. It is also great quality. We are pleased with the cover and I would recommend it to anyone who wants a great fit and strong cover."</p>
    </div>
    <div class="review">
      <span class="review-name">Tariq</span><span class="stars">★★★★★</span>
      <p style="line-height:16px">"I have this on my Ravello and it fits great. I feel better with my car covered and this is a very nice cover. The price was nice especially if you have seen the price on factory covers. I would definitely buy this again and recommend to anyone with car."</p>
    </div>
    <span class="btn-dark">View All Reviews</span>
  </div>

  <section class="band products">
    <h2>Our Products</h2>
    <div class="abs card" style="left:90px">
      <div class="card-photo" role="img" aria-label="Grey drawstring storage bag"></div>
      <div class="card-body">
        <h3>Car Cover Storage Bag</h3>
        <div class="free">Free:</div>
        <ul><li>Breathable Mesh</li><li>Convenient Draw Cord</li><li>Light Weight</li></ul>
      </div>
    </div>
    <div class="abs card" style="left:462px">
      <div class="card-photo" role="img" aria-label="Cable lock with padlock, keys and antenna patch"></div>
      <div class="card-body">
        <h3>Cable Lock &amp; Antenna Patch</h3>
        <div class="free">Free:</div>
        <ul><li>Cable, Lock &amp; Keys</li><li>Reinforcment for Antennas</li></ul>
      </div>
    </div>
  </section>

  <section class="band signup">
    <div class="abs signup-label">Sign Up For Special Email Offers?</div>
    <div class="abs signup-input"></div>
    <div class="abs signup-btn">Sign Up</div>
  </section>

  <footer class="band footer">
    <div class="abs col" style="left:90px"><h4>Customer Service</h4><ul><li>Contact Us</li><li>Returns/Exchanges</li><li>Returns/Exchange Policy</li><li>Secure Shopping / Privacy Policy</li><li>About Us</li><li>Wholesale</li><li>Warranty</li></ul></div>
    <div class="abs col" style="left:236px"><h4>Boat Covers</h4><ul><li>Boat Covers</li><li>Pontoon Covers</li><li>Jet Ski Covers</li></ul></div>
    <div class="abs col" style="left:378px"><h4>Car Covers</h4><ul><li>Car Covers</li><li>SUV Covers</li><li>Truck Covers</li><li>Van Covers</li></ul></div>
    <div class="abs col" style="left:524px"><h4>Motorsport Covers</h4><ul><li>Motorcycle Covers</li><li>ATV Covers</li><li>UTV Covers</li><li>Scooter Covers</li><li>Snowmobile Covers</li></ul></div>
    <div class="abs col" style="left:667px"><h4>Truck Covers</h4><ul><li>Truck Covers</li><li>SUV Covers</li><li>Off-Road Covers</li><li>Van Covers</li></ul></div>
    <div class="abs chat"><svg width="10" height="8" viewBox="0 0 10 8"><rect x=".5" y=".5" width="9" height="7" fill="#fff"/><path d="M.5 .5l4.5 4 4.5-4" fill="none" stroke="#e0241c"/></svg>Leave a message</div>
    <div class="abs payments" role="img" aria-label="Accepted payment cards"><span></span><span></span><span></span><span></span></div>
    <div class="abs footer-rule"></div>
    <div class="abs copy">© 2016 <b>Tide Guard Hoods</b> - All Rights Reserved.</div>
  </footer>

</div>
</div>
</body>
</html>
```